GLS biz card

We need a business card design for our new company based in Los Angeles called "Gold Lantern Studios". We develop film and television projects. We work with investors, financiers, film production companies, film distribution and sales companies as well as studios. We would like to incorporate our logo (see attached) on a two-sided card. We need to include: name and title, address, phone, email and company website.

Target Market(s)

Business, financial and studio clients

Industry/Entity Type

Business

Contact Information for Business Card

Two-sided. We are thinking of the logo on one side and the information on the back. Please feel free to be creative! Thanks.

Requirements
Must have
• Please include the following text information, excluding the "CAPS CATEGORY:" and please allow the ability for us to change the name, title and email address for each company employee):
• NAME & TITLE:
• Peter Dunmore
• Managing Partner
• COMPANY NAME:
• GOLD LANTERN STUDIOS (please use existing logo)
• COMPANY ADDRESS:
• KVT Arts Park
• 2480 Wexley Boulevard
• Arts Hall, 4th Floor
• Manhattan Beach, CA 90266
• COMPANY PHONE NUMBER:
• 310-555-4206
• COMPANY WEBSITE ADDRESS:
• www.goldlanternstudioshouse.com
• EMAIL ADDRESS: (only one per card)
• frank@goldlanternstudioshouse.com
• tizzy@goldlanternstudioshouse.com
• peter@goldlanternstudioshouse.com

```html
<!DOCTYPE html>
<html lang="en">
<head>
<meta charset="utf-8">
<title>Gold Lantern Studios – Business Card</title>
<link href="https://fonts.googleapis.com/css2?family=Source+Sans+3:wght@400;600;700&display=swap" rel="stylesheet">
<style>
  :root {
    --canvas: #d8d5d0;
    --card-black: #070809;
    --strip-black: #111315;
    --cyan: #1ec8f0;
    --cyan-deep: #0a7fa6;
    --teal-dark: #0d2f38;
    --teal-mid: #1d5463;
    --sprocket: #eceeef;
    --ink: #07161c;
    --tagline: #e6eef1;
  }
  * { box-sizing: border-box; margin: 0; padding: 0; }
  html, body {
    width: 1200px;
    height: 900px;
    overflow: hidden;
    background: var(--canvas);
    font-family: "Source Sans 3", Arial, sans-serif;
  }
  .card {
    position: absolute;
    left: 290px;
    width: 620px;
    height: 354px;
    background: var(--card-black);
    border-radius: 3px;
    overflow: hidden;
  }
  .card--front { top: 72px; }
  .card--back { top: 474px; background: var(--strip-black); }

  /* Front */
  .brand {
    position: absolute;
    left: 0; right: 0;
    top: 64px;
    display: flex;
    flex-direction: column;
    align-items: center;
  }
  .brand__dot {
    width: 88px;
    height: 88px;
    border-radius: 50%;
    background: var(--cyan);
    margin-bottom: 26px;
  }
  .brand__name {
    color: var(--cyan);
    font-weight: 600;
    font-size: 30px;
    letter-spacing: 4px;
    line-height: 1;
  }
  .brand__tagline {
    margin-top: 12px;
    color: var(--tagline);
    font-size: 10px;
    letter-spacing: 3px;
  }

  /* Back: film strip */
  .sprockets {
    position: absolute;
    left: 0; right: 0;
    display: flex;
    justify-content: space-around;
    padding: 0 18px;
  }
  .sprockets--top { top: 20px; }
  .sprockets--bottom { bottom: 20px; }
  .sprocket {
    width: 26px;
    height: 24px;
    border-radius: 4px;
    background: var(--sprocket);
  }
  .frame {
    position: absolute;
    top: 66px;
    height: 220px;
    background: linear-gradient(135deg, var(--teal-mid), var(--teal-dark));
  }
  .frame--left { left: 0; width: 66px; }
  .frame--right { left: 506px; width: 114px; }
  .frame--main {
    left: 88px;
    width: 396px;
    background: radial-gradient(circle at 52% 48%, #7fe3fb 0%, var(--cyan) 38%, var(--cyan-deep) 70%, var(--teal-dark) 100%);
    display: flex;
    flex-direction: column;
    justify-content: center;
    align-items: center;
  }
  .contact {
    width: 360px;
    color: var(--ink);
    text-align: center;
  }
  .contact__item {
    padding: 2px 0 3px;
    border-bottom: 1.5px solid var(--ink);
    margin: 0 40px;
  }
  .contact__item:last-child { border-bottom: none; margin: 0; }
  .contact__label {
    font-size: 12px;
    line-height: 1.1;
    text-transform: uppercase;
  }
  .contact__label--mixed { text-transform: none; }
  .contact__value {
    font-size: 15px;
    font-weight: 700;
    line-height: 1.15;
    white-space: nowrap;
  }
  .contact__value--address { font-size: 14px; }
</style>
</head>
<body>
  <section class="card card--front" aria-label="Card front">
    <div class="brand">
      <div class="brand__dot"></div>
      <div class="brand__name">GOLD LANTERN STUDIOS</div>
      <div class="brand__tagline">A MEDIA ENTERTAINMENT COMPANY</div>
    </div>
  </section>

  <section class="card card--back" aria-label="Card back">
    <div class="sprockets sprockets--top">
      <span class="sprocket"></span><span class="sprocket"></span><span class="sprocket"></span>
      <span class="sprocket"></span><span class="sprocket"></span><span class="sprocket"></span>
      <span class="sprocket"></span><span class="sprocket"></span><span class="sprocket"></span>
    </div>

    <div class="frame frame--left"></div>
    <div class="frame frame--main">
      <div class="contact">
        <div class="contact__item">
          <div class="contact__label">Managing Partner</div>
          <div class="contact__value">Peter Dunmore</div>
        </div>
        <div class="contact__item">
          <div class="contact__label contact__label--mixed">E-mail</div>
          <div class="contact__value">peter@goldlanternstudioshouse.com</div>
        </div>
        <div class="contact__item">
          <div class="contact__label">Web</div>
          <div class="contact__value">www.goldlanternstudioshouse.com</div>
        </div>
        <div class="contact__item">
          <div class="contact__label">Phone</div>
          <div class="contact__value">310-555-4206</div>
        </div>
        <div class="contact__item">
          <div class="contact__label">Address</div>
          <div class="contact__value contact__value--address">KVT Arts Park, 2480 Wexley Boulevard, Arts Hall, 4th Floor</div>
          <div class="contact__value contact__value--address">Manhattan Beach, CA 90266</div>
        </div>
      </div>
    </div>
    <div class="frame frame--right"></div>

    <div class="sprockets sprockets--bottom">
      <span class="sprocket"></span><span class="sprocket"></span><span class="sprocket"></span>
      <span class="sprocket"></span><span class="sprocket"></span><span class="sprocket"></span>
      <span class="sprocket"></span><span class="sprocket"></span><span class="sprocket"></span>
    </div>
  </section>
</body>
</html>
```